starlitmanesandtails pet therapy animals

I would like a business card to genarate posative emotions within people. My program has been running in a retirement village for over 5 years I work with residents and family members. My dogs work in palative care and are a great support to family members at the end stage. I also support the families and friends at furnerals when needed to dogs are always with me. Starlitmanes started with the death of my first therapy dog Oscar there was such an out cry of grief within the town and retirement village that he had his own furneral The hooves came into it when I was donated a beautiful Miniature horse for the pet therapy program with great results. I now need something very special as a business card. Eg Angelwings my dogs are King Charles Cavaliers so with what I have described can you create something beautiful to acknowledge to work I do and promote it more.
Updates

Project Deadline Extended
Reason: The reason I have extended the deadline to give other designers a chance to look at the job. So far I have 3 designs. I am hoping to get a few more.

Industry/Entity Type

Town

Contact Information for Business Card

Starlitmanesandtails pet therapy animals
Rosalind Tweedy
E-mail starlitmanesandtails@quillnet.example
Mobile 0461287039
Pet therapy animals give unconditional love to the aged and disabled.

Font styles to use
Decorative

Colors

Designer to choose colors to be used in the design.

Requirements
Nice to have
• angelwings a King Charles Cavalier tan and white with angel wings and a horse with angel wings

```html
<!DOCTYPE html>
<html lang="en">
<head>
<meta charset="utf-8">
<title>Starlitmanesandtails – Business Card</title>
<link rel="stylesheet" href="https://fonts.googleapis.com/css2?family=Arimo:ital,wght@0,400;0,700;1,700&display=swap">
<style>
  :root {
    --ink: #8e3a3a;
    --ink-deep: #8a2c2c;
    --paper: #ffffff;
    --rule: #3a3a3a;
    --sketch-light: #f4f4f4;
    --sketch-mid: #d9d9d9;
    --paw-pink: #f6d6d6;
  }
  html, body {
    margin: 0;
    padding: 0;
    width: 1200px;
    height: 301px;
    overflow: hidden;
    background: var(--paper);
  }
  .sheet {
    position: relative;
    width: 1200px;
    height: 301px;
    box-sizing: border-box;
    border: 1px solid var(--rule);
    background: var(--paper);
    font-family: "Arimo", Arial, sans-serif;
    color: var(--ink);
  }
  .card-divider {
    position: absolute;
    left: 602px;
    top: 0;
    width: 1px;
    height: 100%;
    background: var(--rule);
  }
  .mascot-art {
    position: absolute;
    left: 12px;
    top: 4px;
    width: 300px;
    height: 268px;
    border-radius: 40% 45% 35% 40%;
    background: radial-gradient(ellipse at 55% 45%, var(--sketch-mid) 0%, var(--sketch-light) 60%, var(--paper) 100%);
  }
  .service-title {
    position: absolute;
    left: 300px;
    top: 14px;
    width: 240px;
    text-align: center;
    font-size: 30px;
    line-height: 36px;
    font-weight: 400;
  }
  .brand-name {
    position: absolute;
    right: 608px;
    top: 246px;
    font-size: 32px;
    line-height: 36px;
    font-weight: 700;
    color: var(--ink);
  }
  .paw-trail {
    position: absolute;
    left: 622px;
    top: 0;
    width: 72px;
    height: 300px;
    background: linear-gradient(180deg, var(--paw-pink) 0%, #fbeaea 50%, var(--paw-pink) 100%);
    opacity: 0.7;
  }
  .holder-name {
    position: absolute;
    left: 741px;
    top: 52px;
    font-size: 30px;
    line-height: 34px;
    font-weight: 400;
    letter-spacing: 0.5px;
  }
  .tagline {
    position: absolute;
    left: 625px;
    top: 101px;
    width: 560px;
    margin: 0;
    font-size: 20px;
    line-height: 30px;
    font-weight: 700;
    font-style: italic;
    color: var(--ink-deep);
  }
  .contact-mobile {
    position: absolute;
    left: 881px;
    top: 194px;
    font-size: 23px;
    line-height: 28px;
    font-weight: 700;
  }
  .contact-email {
    position: absolute;
    left: 625px;
    top: 247px;
    font-size: 19px;
    line-height: 24px;
    font-weight: 700;
    white-space: nowrap;
  }
</style>
</head>
<body>
  <div class="sheet">
    <section class="card-front">
      <div class="mascot-art" role="img" aria-label="Pencil sketch of a winged miniature horse leaping"></div>
      <div class="service-title">Pet therapy<br>animals</div>
      <div class="brand-name">Starlitmanesandtails</div>
    </section>

    <div class="card-divider"></div>

    <section class="card-back">
      <div class="paw-trail" role="img" aria-label="Trail of pale pink paw prints running down the card"></div>
      <div class="holder-name">Rosalind Tweedy</div>
      <p class="tagline">Pet therapy animals give unconditional love<br>to the aged and disabled.</p>
      <div class="contact-mobile">Mobile: 0461287039</div>
      <div class="contact-email">E-mail:starlitmanesandtails@quillnet.example</div>
    </section>
  </div>
</body>
</html>
```